Chiropractic healthcare group business card

We are a Portland Oregon based chiropractic healthcare group. Looking for a new business card design. Something cutting edge, that shows off our new logo and tag line.Use either of the attached logos.Our tag line = "Who would you be without pain?"I'm open to about anything, impress me!!
Target Market(s)
Chiropractic patients - Auto injury, back pain, sports injuries, neck , shoulder, hip, knee, ankle pain.
Industry/Entity Type
Chiropractic
Contact Information for Business Card
Dr. Bram Holtvick, D.C.
Clinic name - Fernway Chiropractic
2 clinics
location #1
20418 NW Marwick Road
Suite B
North Plains, OR 97133
Location #2
13529 SE Calloway Street
Portland OR 97236
Main phone line 971.555.0143
website : www.FernwayClinics.example
Tag line "Who would you be without pain?"
Colors
Designer to choose colors to be used in the design.
Requirements
Must have
- Use the logo colors -- Want the orange color to be a TRUE orange.
- Both clinic address
- phone number
- website
- personal email - b.holtvick@ReliefBeginsHere.example
- tag line - "Who would you be without pain?"

```html
<!DOCTYPE html>
<html lang="en">
<head>
<meta charset="utf-8">
<title>Fernway Chiropractic – Business Card</title>
<link rel="stylesheet" href="https://fonts.googleapis.com/css2?family=Outfit:wght@400;500;600&display=swap">
<style>
  :root {
    --page: #ffffff;
    --card: #d3d4d6;
    --ink: #636363;
    --orange: #f59824;
  }
  * { margin: 0; padding: 0; box-sizing: border-box; }
  html, body {
    width: 1200px; height: 1200px; overflow: hidden;
    background: var(--page);
    font-family: "Outfit", sans-serif;
    color: var(--ink);
  }
  .canvas { position: relative; width: 1200px; height: 1200px; }
  .card {
    position: absolute; left: 32px; top: 279px;
    width: 1140px; height: 648px;
    background: var(--card);
    overflow: hidden;
  }
  .bands { position: absolute; left: 0; top: 0; width: 1140px; height: 648px; }

  .brand {
    position: absolute; left: 50px; top: 175px;
    width: 330px;
    display: flex; align-items: center; gap: 18px;
  }
  .brand-square { width: 34px; height: 34px; background: var(--orange); flex: none; }
  .brand-name {
    font-weight: 600; font-size: 44px; line-height: 1.05;
    letter-spacing: 1px; color: var(--ink);
  }

  .doctor {
    position: absolute; left: 598px; top: 130px;
    font-weight: 600; font-size: 44px; letter-spacing: -1.5px;
    line-height: 1; white-space: nowrap;
  }
  .doctor-rule {
    position: absolute; left: 598px; top: 182px;
    width: 398px; height: 9px; background: var(--orange);
  }
  .doctor-rule::before {
    content: ""; position: absolute; left: 0; top: 0;
    width: 90px; height: 9px; background: var(--ink);
  }

  .contact-icon {
    position: absolute; width: 36px; height: 36px;
    background: var(--orange);
    display: flex; align-items: center; justify-content: center;
  }
  .contact-icon svg { width: 26px; height: 26px; }
  .icon-phone { left: 619px; top: 294px; }
  .icon-web { left: 618px; top: 364px; }
  .icon-pin { left: 620px; top: 442px; }

  .contact-text {
    position: absolute; font-weight: 600; white-space: nowrap;
  }
  .phone { left: 673px; top: 300px; font-size: 23px; }
  .web { left: 673px; top: 370px; font-size: 23px; font-weight: 500; }
  .address {
    left: 667px; top: 412px;
    font-size: 22px; line-height: 24px; font-weight: 500;
  }
</style>
</head>
<body>
<div class="canvas">
  <section class="card">
    <svg class="bands" viewBox="0 0 1140 648" aria-hidden="true">
      <polygon points="0,464 122,464 189,557 0,557" fill="var(--orange)"/>
      <polygon points="122,464 281,464 348,557 189,557" fill="var(--ink)"/>
      <polygon points="315,464 474,464 545,572 1140,572 1140,605 412,605" fill="var(--orange)"/>
    </svg>

    <div class="brand">
      <span class="brand-square"></span>
      <span class="brand-name">Fernway<br>Chiropractic</span>
    </div>

    <h1 class="doctor">Dr. Bram Holtvick, D.C.</h1>
    <div class="doctor-rule"></div>

    <span class="contact-icon icon-phone">
      <svg viewBox="0 0 26 26" aria-hidden="true">
        <rect x="7.5" y="1.5" width="11" height="23" rx="1.5" fill="none" stroke="var(--ink)" stroke-width="1.6"/>
        <line x1="11" y1="3.5" x2="15" y2="3.5" stroke="var(--ink)" stroke-width="1"/>
        <circle cx="13" cy="22" r="0.9" fill="var(--ink)"/>
      </svg>
    </span>
    <p class="contact-text phone">971.555.0143</p>

    <span class="contact-icon icon-web">
      <svg viewBox="0 0 26 26" aria-hidden="true">
        <circle cx="13" cy="13" r="11.5" fill="var(--ink)"/>
        <path d="M2 10 Q13 15 24 10 M2 14 Q13 19 24 14 M3 18 Q13 22 23 18" fill="none" stroke="var(--orange)" stroke-width="1.2"/>
      </svg>
    </span>
    <p class="contact-text web">www.FernwayClinics.example</p>

    <span class="contact-icon icon-pin">
      <svg viewBox="0 0 26 26" aria-hidden="true">
        <path d="M13 2 C7.5 2 4.5 6 4.5 10 C4.5 15 13 24.5 13 24.5 C13 24.5 21.5 15 21.5 10 C21.5 6 18.5 2 13 2 Z" fill="var(--ink)"/>
        <circle cx="13" cy="10" r="3.3" fill="var(--orange)"/>
      </svg>
    </span>
    <p class="contact-text address">
      Street#1: 13529 SE Calloway Street Portland,<br>
      OR 97236.<br>
      Street#2: 20418 NW Marwick Road Suite<br>
      B North Plains, OR 97133.
    </p>
  </section>
</div>
</body>
</html>
```